依頼詳細
既存サイトのデザインが古くなったため、リニューアルを行います。
ワイヤーフレーム有。
参考サイト有。
https://www.morisuzu-web.jp/
今風でシンプルなデザインをお願いいたします。
メインカラーは緑で、現在のロゴをお渡ししますので、トレースしSVGで作ってください。
サイトURL
ページ数
1ページ
希望イメージ
シンプル 複雑
単色 カラフル
暗い 明るい
日常 高級
遊び心 厳粛
未来的 伝統的
女性的 男性的
希望する色
緑系
納品ファイル
• イラストレーター形式 (.ai)
補足説明
TOPページ(PC版とスマホ版)のみご提案ください。
採用した場合は、アーカイブと詳細ページ(スタイルガイド)のデザインもお願いいたします。
ワイヤーフレームではなく、サイトマップ有です。
締め切りを10日後に変更しました。
URLの記載があるのは、参考サイトです。
会社名はダミー(株式会社ダミーリサイクル)とし、
添付のサイトマップに合わせて作っていただけると幸いです。
記載内容がややこしくて申し訳ございません。
その他文言等もダミーで結構です。
よろしくお願いいたします。
■ 選んだ理由

シンプルかつ、今風なレイアウトで好感が持てました。

■ 提案者全員のお礼・コメント

修正依頼にも迅速に対応いただき、ありがとうございました。
またご提案よろしくお願いいたします。

```html
<!DOCTYPE html>
<html lang="ja">
<head>
<meta charset="UTF-8">
<title>株式会社ダミーリサイクル</title>
<link href="https://fonts.googleapis.com/css2?family=Noto+Sans+JP:wght@400;500;700&family=Montserrat:wght@400;500&display=swap" rel="stylesheet">
<style>
:root{
  --green:#3f9c3a;
  --green-dark:#2f7f2c;
  --text:#333333;
  --muted:#777777;
  --line:#cccccc;
  --light-gray:#c8c8c8;
  --mid-gray:#a3a3a3;
  --bg-gray:#f3f3f3;
  --white:#ffffff;
}
*{margin:0;padding:0;box-sizing:border-box}
html,body{width:1200px;height:3768px;overflow:hidden}
body{position:relative;background:var(--white);color:var(--text);font-family:"Noto Sans JP",sans-serif}
.abs{position:absolute}
.en{font-family:"Montserrat","Noto Sans JP",sans-serif;letter-spacing:.15em}

/* hero */
.hero{left:0;top:0;width:1200px;height:740px;background:linear-gradient(180deg,#1f4d22 0%,#2f7a32 35%,#4e9c44 70%,#3a7c35 100%)}
.site-logo{left:40px;top:48px;font-size:26px;font-weight:700;color:var(--white);letter-spacing:.04em}
.top-links{top:22px;right:60px;display:flex;gap:28px}
.top-link{border:1px solid var(--white);color:var(--white);font-size:12px;padding:5px 16px}
.global-nav{top:68px;right:40px;display:flex;gap:34px;color:var(--white);font-size:14px;font-weight:500}
.catch{left:0;top:328px;width:1200px;text-align:center;color:var(--white);font-size:34px;font-weight:500;letter-spacing:.08em}

/* news */
.news{left:160px;top:628px;width:872px;height:240px;background:var(--white);box-shadow:0 6px 24px rgba(0,0,0,.15)}
.news-title{left:48px;top:88px;font-size:32px;font-weight:500}
.news-sub{left:50px;top:138px;font-size:11px;color:var(--muted)}
.news-list{left:304px;top:28px;width:380px}
.news-item{border-bottom:1px dashed var(--line);padding:6px 0 10px;margin-bottom:10px}
.news-date{font-size:11px;color:var(--muted)}
.news-text{font-size:13px;margin-top:2px}
.btn{border:1px solid var(--text);font-size:11px;text-align:center;background:var(--white)}
.news-more{left:704px;top:188px;width:152px;height:32px;line-height:30px}

/* section titles */
.sec-title{left:0;width:1200px;text-align:center;font-size:38px;font-weight:500}
.sec-sub{left:0;width:1200px;text-align:center;font-size:12px;color:var(--text)}

/* business */
.biz{top:1156px;width:400px;height:400px;color:var(--white);text-align:center}
.biz-photo{position:absolute;inset:0}
.biz-shade{position:absolute;inset:0;background:rgba(0,0,0,.35)}
.biz-body{position:absolute;left:0;top:110px;width:400px}
.biz-name{font-size:22px;font-weight:500;margin-bottom:24px}
.biz-desc{font-size:13px;line-height:1.8}
.biz-more{display:inline-block;margin-top:40px;width:150px;height:30px;line-height:28px;border:1px solid var(--white);font-size:11px}

/* products */
.product{top:1824px;width:288px;height:296px;display:flex;align-items:center;justify-content:center;color:var(--white);font-size:14px}
.product.light{background:var(--light-gray)}
.product.dark{background:var(--mid-gray)}
.arrow{top:1950px}

/* info links */
.info{height:240px;background:var(--green);color:var(--white)}
.info-photo{position:absolute;top:0;right:0;width:55%;height:100%;background:linear-gradient(90deg,rgba(63,156,58,1) 0%,rgba(120,180,110,.6) 60%,rgba(180,210,170,.5) 100%)}
.info-title{position:absolute;top:82px;font-size:36px;font-weight:500}
.info-sub{position:absolute;top:136px;font-size:11px}
.info-arrow{position:absolute;top:100px}

/* column */
.column-sec{left:0;top:2700px;width:1200px;height:620px;background:var(--bg-gray)}
.col-card{top:2924px;width:216px}
.col-photo{width:216px;height:144px;background:linear-gradient(135deg,#e6f2f5 0%,#a9d69a 50%,#4f9e46 100%)}
.col-date{font-size:11px;color:var(--muted);margin-top:34px}
.col-text{font-size:13px;font-weight:500;margin-top:14px}

/* footer */
.foot-logo{left:160px;top:3402px;font-size:22px;font-weight:700}
.foot-addr{left:160px;top:3452px;font-size:12px;line-height:2.6}
.map-btn{left:160px;top:3572px;width:150px;height:36px;line-height:34px;font-size:12px}
.foot-nav{left:540px;display:flex;gap:36px;font-size:13px}
.follow{left:540px;top:3582px;display:flex;align-items:center;gap:20px;font-size:12px}
.sns{font-size:12px;font-weight:500}
.page-top{left:1032px;top:3600px;width:64px;height:64px;background:var(--green);color:var(--white);font-size:10px;display:flex;align-items:center;justify-content:center}
.copy{left:0;top:3688px;width:1200px;height:80px;background:var(--green);color:var(--white);font-size:12px;text-align:center;line-height:80px}
</style>
</head>
<body>

<header>
  <div class="abs hero" role="img" aria-label="緑の針葉樹林の写真"></div>
  <div class="abs site-logo">株式会社ダミーリサイクル</div>
  <div class="abs top-links">
    <span class="top-link">お問い合わせ</span>
    <span class="top-link">アクセス・会社概要</span>
  </div>
  <nav class="abs global-nav">
    <span>企業情報</span><span>事業紹介</span><span>商品情報</span><span>コラム</span><span>採用情報</span><span>お問い合わせ</span>
  </nav>
  <p class="abs catch">キャッチコピーがはいります。</p>
</header>

<section class="abs news">
  <h2 class="abs news-title">お知らせ</h2>
  <p class="abs news-sub en">NEWS</p>
  <div class="abs news-list">
    <div class="news-item"><p class="news-date">2020.xx.xx</p><p class="news-text">ホームページをリニューアルしました。</p></div>
    <div class="news-item"><p class="news-date">2020.xx.xx</p><p class="news-text">お知らせのタイトルが入ります。</p></div>
    <div class="news-item"><p class="news-date">2020.xx.xx</p><p class="news-text">お知らせのタイトルが入ります。</p></div>
  </div>
  <div class="abs btn news-more en">MORE</div>
</section>

<h2 class="abs sec-title" style="top:1004px">事業紹介</h2>
<p class="abs sec-sub en" style="top:1060px">BUSINESS</p>

<section>
  <div class="abs biz" style="left:0">
    <div class="biz-photo" role="img" aria-label="高層ビルが並ぶ街並みの写真" style="background:linear-gradient(180deg,#7fa7c9,#3c5d80)"></div>
    <div class="biz-shade"></div>
    <div class="biz-body"><p class="biz-name">販売事業</p><p class="biz-desc">テキストが入ります。テキストが入ります。<br>テキストが入ります。テキスト。</p><span class="biz-more en">MORE</span></div>
  </div>
  <div class="abs biz" style="left:400px">
    <div class="biz-photo" role="img" aria-label="並んだトラックの写真" style="background:linear-gradient(180deg,#b9bec4,#5d6168)"></div>
    <div class="biz-shade"></div>
    <div class="biz-body"><p class="biz-name">運搬事業</p><p class="biz-desc">テキストが入ります。テキストが入ります。<br>テキストが入ります。テキスト。</p><span class="biz-more en">MORE</span></div>
  </div>
  <div class="abs biz" style="left:800px">
    <div class="biz-photo" role="img" aria-label="木造建築の骨組みの写真" style="background:linear-gradient(180deg,#c99a66,#6f4a28)"></div>
    <div class="biz-shade"></div>
    <div class="biz-body"><p class="biz-name">建築事業</p><p class="biz-desc">テキストが入ります。テキストが入ります。<br>テキストが入ります。テキスト。</p><span class="biz-more en">MORE</span></div>
  </div>
</section>

<h2 class="abs sec-title" style="top:1672px">商品情報</h2>
<p class="abs sec-sub en" style="top:1728px">PRODUCT</p>

<section>
  <div class="abs product light" style="left:-128px">商品の説明がはいります。</div>
  <div class="abs product dark" style="left:160px">商品の説明がはいります。</div>
  <div class="abs product light" style="left:448px">商品の説明がはいります。</div>
  <div class="abs product dark" style="left:736px">商品の説明がはいります。</div>
  <div class="abs product light" style="left:1024px">商品の説明がはいります。</div>
  <svg class="abs arrow" style="left:120px" width="24" height="40" viewBox="0 0 24 40"><polyline points="20,4 4,20 20,36" fill="none" stroke="#fff" stroke-width="3"/></svg>
  <svg class="abs arrow" style="left:1050px" width="24" height="40" viewBox="0 0 24 40"><polyline points="4,4 20,20 4,36" fill="none" stroke="#fff" stroke-width="3"/></svg>
</section>

<a class="abs info" style="left:0;top:2244px;width:552px">
  <div class="info-photo" role="img" aria-label="オフィスで働く人の手元の写真"></div>
  <span class="info-title" style="left:80px">会社情報</span>
  <span class="info-sub en" style="left:82px">COMPANY</span>
  <svg class="info-arrow" style="left:480px" width="24" height="40" viewBox="0 0 24 40"><polyline points="4,4 20,20 4,36" fill="none" stroke="#fff" stroke-width="3"/></svg>
</a>
<a class="abs info" style="left:644px;top:2356px;width:556px">
  <div class="info-photo" role="img" aria-label="笑顔で働く女性スタッフの写真"></div>
  <span class="info-title" style="left:60px">求人情報</span>
  <span class="info-sub en" style="left:62px">RECRUIT</span>
  <svg class="info-arrow" style="left:484px" width="24" height="40" viewBox="0 0 24 40"><polyline points="4,4 20,20 4,36" fill="none" stroke="#fff" stroke-width="3"/></svg>
</a>

<section class="abs column-sec"></section>
<h2 class="abs sec-title" style="top:2792px">コラム</h2>
<p class="abs sec-sub en" style="top:2848px">COLUMN</p>
<article class="abs col-card" style="left:232px"><div class="col-photo" role="img" aria-label="四つ葉のクローバーの写真"></div><p class="col-date">2020.x.x.x.x</p><p class="col-text">タイトルが入ります。</p></article>
<article class="abs col-card" style="left:504px"><div class="col-photo" role="img" aria-label="白い花と植物の写真"></div><p class="col-date">2020.x.x.x.x</p><p class="col-text">タイトルが入ります。</p></article>
<article class="abs col-card" style="left:780px"><div class="col-photo" role="img" aria-label="四つ葉のクローバーの写真"></div><p class="col-date">2020.x.x.x.x</p><p class="col-text">タイトルが入ります。</p></article>

<footer>
  <p class="abs foot-logo">株式会社ダミーリサイクル</p>
  <p class="abs foot-addr">〒000-0000<br>緑山市森町1-2-3<br>TEL　000-000-0000</p>
  <div class="abs btn map-btn">Area Map</div>
  <nav class="abs foot-nav" style="top:3410px"><span>企業情報</span><span>事業紹介</span><span>商品情報</span><span>コラム</span><span>採用情報</span><span>お問い合わせ</span></nav>
  <nav class="abs foot-nav" style="top:3474px"><span>関連会社情報</span><span>プライバシーポリシー</span><span>サイトマップ</span></nav>
  <div class="abs follow"><span class="en">Follow us</span><span class="sns">Snap</span><span class="sns">Feed</span></div>
  <div class="abs page-top en">TOP</div>
  <p class="abs copy">© 株式会社ダミーリサイクル</p>
</footer>

</body>
</html>
```